BrickPlayo Business Card

We need a business card design for our company. We sell construction-themed amusement rides for kids.

Contact Information for Business Card

Contact info on business card should include:
Lars Wendt
Co-Founder & COO
(833) 527-BRIKPLA
Lars@brickplayo.com
www.brickplayo.com

```html
<!DOCTYPE html>
<html lang="en">
<head>
<meta charset="utf-8">
<title>BrickPlayo Business Card</title>
<link rel="stylesheet" href="https://fonts.googleapis.com/css2?family=Arimo:wght@400;700&display=swap">
<style>
  :root {
    --page-bg: #e9e7e4;
    --card-grey: #7d7e81;
    --card-shadow: rgba(0, 0, 0, 0.25);
    --text-white: #ffffff;
    --brand-orange: #e2541c;
    --brand-silver: #c9cacc;
    --art-yellow: #f4c21f;
    --art-blue: #3d5a9c;
    --art-orange: #e85a2a;
  }
  html, body {
    margin: 0;
    width: 1200px;
    height: 844px;
    overflow: hidden;
    background: var(--page-bg);
    font-family: "Arimo", Arial, sans-serif;
  }
  .card {
    position: absolute;
    top: 267px;
    width: 540px;
    height: 310px;
    background: var(--card-grey);
    box-shadow: 0 8px 24px var(--card-shadow);
    overflow: hidden;
  }
  .card--front { left: 40px; }
  .card--back { left: 620px; }

  .brand {
    position: absolute;
    display: flex;
    align-items: center;
    gap: 10px;
    font-weight: 700;
  }
  .brand__mark {
    width: 22px;
    height: 22px;
    border-radius: 50%;
  }
  .card--front .brand {
    left: 34px;
    top: 70px;
    color: var(--brand-orange);
    font-size: 36px;
  }
  .card--front .brand__mark { background: var(--brand-orange); }
  .card--back .brand {
    left: 50%;
    top: 50%;
    transform: translate(-50%, -50%);
    color: var(--brand-silver);
    font-size: 52px;
  }
  .card--back .brand__mark {
    width: 32px;
    height: 32px;
    background: var(--brand-silver);
  }

  .artwork {
    position: absolute;
    right: 18px;
    top: 42px;
    width: 262px;
    height: 236px;
    border-radius: 40px 40px 12px 12px;
    background: linear-gradient(160deg, var(--art-yellow) 0%, var(--art-orange) 45%, var(--art-blue) 100%);
    opacity: 0.85;
  }

  .contact {
    position: absolute;
    left: 34px;
    top: 150px;
    color: var(--text-white);
  }
  .contact__name {
    margin: 0;
    font-size: 22px;
    font-weight: 700;
    letter-spacing: 0.5px;
  }
  .contact__title {
    margin: 2px 0 14px;
    font-size: 16px;
  }
  .contact__list {
    list-style: none;
    margin: 0;
    padding: 0;
    font-size: 15px;
  }
  .contact__item {
    display: flex;
    align-items: center;
    gap: 9px;
    margin-bottom: 5px;
  }
  .contact__icon {
    width: 15px;
    height: 15px;
    flex: none;
  }
</style>
</head>
<body>
  <section class="card card--front">
    <div class="brand"><span class="brand__mark"></span>BrickPlayo</div>

    <div class="artwork" role="img" aria-label="Illustration of two cartoon construction workers in hard hats shaking hands"></div>

    <div class="contact">
      <h1 class="contact__name">LARS WENDT</h1>
      <p class="contact__title">Co-Founder &amp; COO</p>
      <ul class="contact__list">
        <li class="contact__item">
          <svg class="contact__icon" viewBox="0 0 16 16" aria-hidden="true"><rect x="0.75" y="0.75" width="14.5" height="14.5" rx="2" fill="none" stroke="#fff" stroke-width="1.5"/><path d="M5 4l2 2-1 1.2c.6 1.2 1.6 2.2 2.8 2.8L10 9l2 2-1.3 1.3C7.5 12 4 8.5 3.7 5.3z" fill="#fff"/></svg>
          (833) 527-BRIKPLA
        </li>
        <li class="contact__item">
          <svg class="contact__icon" viewBox="0 0 16 16" aria-hidden="true"><rect x="0.5" y="3" width="15" height="10" fill="#fff"/><path d="M0.5 3l7.5 6 7.5-6" fill="none" stroke="#7d7e81" stroke-width="1.2"/></svg>
          Lars@brickplayo.com
        </li>
        <li class="contact__item">
          <svg class="contact__icon" viewBox="0 0 16 16" aria-hidden="true"><circle cx="8" cy="8" r="7.5" fill="#fff"/><g fill="none" stroke="#7d7e81" stroke-width="1"><ellipse cx="8" cy="8" rx="3" ry="7"/><path d="M1 8h14M2 4.5h12M2 11.5h12"/></g></svg>
          www.brickplayo.com
        </li>
      </ul>
    </div>
  </section>

  <section class="card card--back">
    <div class="brand"><span class="brand__mark"></span>BrickPlayo</div>
  </section>
</body>
</html>
```